Briefpapier, Visitenkarten, Bindemappe, Brieumschläge....
Zielgruppe
Steuerberatung vorwiegen für Unternehmer
Aufgabenstellung
Ein Logo ist bereits vorhanden (siehe Analgen) kann aber gerne auch bei einer guten Idee modernisiert werden. Ganz ein neues Logo möchte ich meinen Kunden jedoch ersparen, da ich es erst von zwei Jahren gewechselt habe. Grundfarbe grün wie Pantone 2293 C.
Als Anhaltspunkt was derzeit bei im Einsatz ist, habe ich die entsprechenden Dateien hochgeladen.

```html
<!DOCTYPE html>
<html lang="de">
<head>
<meta charset="utf-8">
<title>Briefpapier – Steuerberater Tobias Lenz</title>
<link href="https://fonts.googleapis.com/css2?family=Source+Sans+3:wght@400;600;700&display=swap" rel="stylesheet">
<style>
  :root {
    --backdrop: #cbcbcb;
    --paper: #ffffff;
    --green-deep: #76b82a;
    --green-light: #c9d400;
    --ink: #1d1d1b;
  }
  * { margin: 0; padding: 0; box-sizing: border-box; }
  html, body {
    width: 1200px; height: 1118px; overflow: hidden;
    background: var(--backdrop);
    font-family: "Source Sans 3", Arial, sans-serif;
    color: var(--ink);
  }
  .letterhead {
    position: absolute;
    left: 246px; top: 57px;
    width: 708px; height: 1002px;
    background: var(--paper);
  }
  .header-band {
    position: absolute; left: 0; top: 0; width: 708px; height: 96px;
    background: linear-gradient(90deg, var(--green-deep), var(--green-light));
  }
  .header-rule {
    position: absolute; left: 0; top: 102px; width: 708px; height: 3px;
    background: linear-gradient(90deg, var(--green-deep), var(--green-light));
  }
  .brand {
    position: absolute; left: 0; top: 16px; width: 708px;
    text-align: center; color: var(--paper); font-weight: 600;
  }
  .brand-mark {
    display: block; width: 22px; height: 22px; margin: 0 auto 6px;
    background: var(--paper);
  }
  .brand-title {
    display: inline-block; font-size: 17px; line-height: 1;
    padding-bottom: 3px; border-bottom: 1.5px solid var(--paper);
  }
  .brand-name {
    display: block; font-size: 9px; line-height: 1; letter-spacing: 1.5px; margin-top: 4px;
  }
  .footer {
    position: absolute; top: 866px;
    font-size: 15px; line-height: 19.5px;
  }
  .footer strong { font-weight: 700; }
  .contact { left: 24px; }
  .bank { left: 288px; }
  .tax { left: 496px; top: 864px; font-size: 19px; line-height: 23px; }
  .footer-stripe {
    position: absolute; left: 0; bottom: 0; width: 708px; height: 8px;
    background: linear-gradient(90deg, var(--green-deep), var(--green-light));
  }
</style>
</head>
<body>
  <div class="letterhead">
    <div class="header-band"></div>
    <div class="header-rule"></div>
    <div class="brand">
      <span class="brand-mark"></span>
      <span class="brand-title">Steuerberater</span>
      <span class="brand-name">Tobias Lenz</span>
    </div>

    <div class="footer contact">
      <strong>Nordlicht Beratung</strong><br>
      Lindenallee 14<br>
      D-56070 Koblenz<br>
      Fon: +49 (0) 261 555 012 30<br>
      Fax: +49 (0) 261 555 012 39<br>
      E-Mail: info@nordlicht-beratung.de
    </div>
    <div class="footer bank">
      <strong>Bankverbindung:</strong><br>
      Nordlicht Beratung<br>
      Stadtbank Koblenz<br>
      Kto.- Nr.: 306915<br>
      BLZ: 570 000 00<br>
      IBAN: DE00 5700 0000 0000 3069 15
    </div>
    <div class="footer tax">
      <strong>Finanzamt Musterstadt</strong><br>
      USt. ID: DE000123456<br>
      St.-Nr.: 00/000/1234/5
    </div>

    <div class="footer-stripe"></div>
  </div>
</body>
</html>
```